Occupational Therapy Clinic Advertisement

Create an advertisement for a magazine. Below I have attached my original ad (Ad 2020.pdf) . I want the ad changed and it should be eye catching. I would like a eye catching graphics added in the ad. It should be a graphic image that applies to education. I am attaching a sample graphic image of that I liked from someone elses ad- it should not be the same- it just is there to show what I like. Please use the same words from my original ad.Dimensions: 3.75in x 10.3 in

Target Market(s)

Parents of School aged children

Requirements
Must have
• Must have eye catching Graphic. Colors should be eye catching for a typed magazine.

```html
<!DOCTYPE html>
<html lang="en">
<head>
<meta charset="utf-8">
<title>Bright Steps OT Services – Magazine Ad</title>
<link href="https://fonts.googleapis.com/css2?family=Arvo:wght@400;700&family=Montserrat:wght@400;600;700&display=swap" rel="stylesheet">
<style>
  :root{
    --stage:#e6e7ea;
    --mint:#dff2ee;
    --mint-light:#f2fbf9;
    --red:#f0330f;
    --red-deep:#d8240a;
    --maroon:#4e1320;
    --blue:#1e9fd6;
    --blue-deep:#1479b8;
    --paper:#fbfaf8;
    --rule:#c9d6d3;
    --text-dark:#3a1a20;
    --text-body:#4a3a3c;
    --skin:#d9a98a;
    --hair:#8a5a3c;
  }
  *{margin:0;padding:0;box-sizing:border-box}
  html,body{width:1200px;height:2851px;overflow:hidden;background:var(--stage)}
  .ad{
    position:absolute;left:125px;top:70px;width:950px;height:2610px;
    background:linear-gradient(180deg,var(--mint) 0%,var(--mint-light) 45%,var(--mint) 72%);
    box-shadow:0 6px 14px rgba(0,0,0,.25);overflow:hidden;
    font-family:"Arvo",serif;
  }
  /* hero artwork */
  .hero-art{
    position:absolute;left:102px;top:113px;width:737px;height:1014px;
    border-radius:260px 260px 40px 40px;
    background:linear-gradient(160deg,var(--blue) 0%,var(--blue-deep) 22%,var(--maroon) 38%,var(--maroon) 52%,var(--red) 64%,var(--red-deep) 100%);
  }
  .hero-shadow{
    position:absolute;left:290px;top:1200px;width:360px;height:26px;border-radius:50%;
    background:radial-gradient(ellipse,rgba(0,0,0,.18),rgba(0,0,0,0) 70%);
  }
  .question{
    position:absolute;color:#fff;font-weight:700;font-size:36px;line-height:1.12;
  }
  .q-reading{left:150px;top:225px;transform:rotate(-12deg)}
  .q-test{left:570px;top:360px;text-align:right;transform:rotate(-12deg)}
  .q-memory{left:420px;top:640px;transform:rotate(18deg)}

  /* headline */
  .headline{
    position:absolute;left:0;top:1280px;width:950px;text-align:center;
    color:var(--red);font-weight:700;font-size:76px;line-height:80px;letter-spacing:-1px;
  }
  .struck{color:var(--maroon);position:relative}
  .struck::after{
    content:"";position:absolute;left:-2px;right:-6px;top:44%;height:4px;
    background:var(--red);transform:rotate(18deg);
  }

  /* features */
  .feature{position:absolute;left:68px;width:440px;height:120px}
  .feature-icon{
    position:absolute;left:3px;top:0;width:106px;height:106px;border-radius:50%;
    border:4px solid var(--red);background:#fff;
    box-shadow:4px 6px 8px rgba(0,0,0,.15);
  }
  .feature-icon svg{position:absolute;left:23px;top:23px}
  .feature-text{position:absolute;left:150px;top:6px;color:var(--text-dark)}
  .feature-title{font-weight:700;font-size:34px;line-height:36px}
  .feature-sub{font-size:27px;line-height:31px;color:var(--text-body)}
  .f-eval{top:1500px}
  .f-treat{top:1654px}
  .f-age{top:1806px}
  .rule{position:absolute;left:85px;width:415px;height:2px;background:linear-gradient(90deg,var(--rule),rgba(201,214,211,0))}
  .r1{top:1635px}.r2{top:1787px}.r3{top:1939px}
  .treat-note{
    position:absolute;left:568px;top:1497px;color:var(--maroon);
    font-weight:700;font-size:37px;line-height:42px;
  }
  .portrait{
    position:absolute;left:511px;top:1668px;width:435px;height:374px;
    border-radius:200px 200px 0 0;
    background:linear-gradient(180deg,var(--hair) 0%,var(--skin) 38%,#e7bfa3 100%);
  }

  /* contact panel */
  .contact{
    position:absolute;left:0;top:2042px;width:950px;height:568px;background:var(--paper);
    font-family:"Montserrat",sans-serif;
  }
  .brand{position:absolute;left:0;top:55px;width:950px;text-align:center;color:var(--maroon);font-weight:700}
  .brand-name{font-size:68px;line-height:70px;letter-spacing:1px}
  .brand-sub{font-size:52px;line-height:58px;display:flex;justify-content:center;align-items:center;gap:18px}
  .brand-sub .arrow-line{width:78px;height:3px;background:var(--maroon);position:relative}
  .brand-phone{font-size:56px;line-height:64px;color:var(--text-dark);margin-top:0}
  .info{position:absolute;left:119px;font-size:26px;line-height:34px;color:var(--text-body)}
  .info-icon{position:absolute;left:-64px;top:4px}
  .i-location{top:285px}
  .i-email{top:405px}
  .email{color:var(--red);font-weight:700}
  .rsa-box{
    position:absolute;left:528px;top:293px;width:350px;height:84px;border:2px solid var(--rule);
    text-align:center;color:var(--maroon);font-size:32px;line-height:38px;padding-top:3px;font-weight:600;
  }
  .therapist{position:absolute;left:518px;top:408px;width:370px;text-align:center}
  .therapist-name{color:var(--red);font-size:31px;line-height:38px;font-weight:600}
  .therapist-phone{color:var(--text-dark);font-size:38px;line-height:46px;font-weight:700}
</style>
</head>
<body>
<main class="ad">
  <div class="hero-art" role="img" aria-label="Illustration of a red pencil bent into a question mark made of puzzle pieces, over faint school doodles"></div>
  <p class="question q-reading">Does your child<br>struggle with<br>Reading/Kriah?</p>
  <p class="question q-test">Knows the<br>information<br>but fails the<br>test?</p>
  <p class="question q-memory">Has difficulty<br>remembering<br>names<br>and<br>dates?</p>
  <div class="hero-shadow"></div>

  <h1 class="headline">Yes Your Child <span class="struck">can</span> Will<br>Succeed in School!</h1>

  <div class="feature f-eval">
    <div class="feature-icon">
      <svg width="60" height="60" viewBox="0 0 60 60" fill="none" stroke="#f0330f" stroke-width="4" stroke-linejoin="round">
        <rect x="8" y="8" width="34" height="44" rx="3"/>
        <rect x="17" y="4" width="16" height="8" rx="2"/>
        <path d="M15 24h20M15 32h14M15 40h10"/>
        <circle cx="44" cy="44" r="10" fill="#fff"/>
        <path d="M44 39v5l4 2"/>
      </svg>
    </div>
    <div class="feature-text">
      <div class="feature-title">We Evaluate</div>
      <div class="feature-sub">Using standardized<br>Evaluations</div>
    </div>
  </div>
  <div class="rule r1"></div>

  <div class="feature f-treat">
    <div class="feature-icon">
      <svg width="60" height="60" viewBox="0 0 60 60" fill="none" stroke="#f0330f" stroke-width="4" stroke-linejoin="round" stroke-linecap="round">
        <path d="M4 10h20a6 6 0 0 1 6 6v34a5 5 0 0 0-5-5H4z"/>
        <path d="M56 10H36a6 6 0 0 0-6 6v34a5 5 0 0 1 5-5h21z"/>
        <path d="M10 20h13M10 28h13M10 36h10"/>
        <circle cx="43" cy="35" r="7" fill="#fff"/>
        <path d="M38 41l-6 7"/>
      </svg>
    </div>
    <div class="feature-text">
      <div class="feature-title">We Treat</div>
      <div class="feature-sub">Using Researched<br>based techniques</div>
    </div>
  </div>
  <div class="rule r2"></div>

  <div class="feature f-age">
    <div class="feature-icon">
      <svg width="60" height="60" viewBox="0 0 60 60" fill="none">
        <path d="M52 22A24 24 0 1 0 52 40" stroke="#f0330f" stroke-width="4" stroke-linecap="round"/>
        <path d="M46 20l8 0 0-8" stroke="#f0330f" stroke-width="4" stroke-linecap="round" stroke-linejoin="round"/>
        <text x="29" y="36" text-anchor="middle" font-family="Montserrat, sans-serif" font-weight="700" font-size="15" fill="#f0330f">AGE</text>
      </svg>
    </div>
    <div class="feature-text">
      <div class="feature-title">Ages</div>
      <div class="feature-sub">6-18</div>
    </div>
  </div>
  <div class="rule r3"></div>

  <p class="treat-note">We Treat the<br>underlying<br>processing deficits</p>
  <div class="portrait" role="img" aria-label="Photo of a young woman peeking up from the lower edge, looking to the side"></div>

  <section class="contact">
    <div class="brand">
      <div class="brand-name">BRIGHT STEPS</div>
      <div class="brand-sub"><span class="arrow-line"></span>OT SERVICES<span class="arrow-line"></span></div>
      <div class="brand-phone">(718) 555-0142</div>
    </div>

    <div class="info i-location">
      <svg class="info-icon" width="30" height="42" viewBox="0 0 30 42"><path d="M15 0C7 0 1 6 1 14c0 10 14 28 14 28s14-18 14-28C29 6 23 0 15 0z" fill="#f0330f"/><circle cx="15" cy="14" r="5" fill="#fbfaf8"/></svg>
      Located in Borough Park<br>Evaluations done in Borough<br>Park &amp; Staten Island
    </div>
    <div class="info i-email">
      <svg class="info-icon" width="38" height="28" viewBox="0 0 38 28"><rect width="38" height="28" rx="3" fill="#f0330f"/><path d="M2 3l17 13L36 3" fill="none" stroke="#fbfaf8" stroke-width="3"/></svg>
      For more information or<br>to be added to our email list,<br><span class="email">brightstepsot@example.com</span>
    </div>

    <div class="rsa-box">Board of Ed<br>OT RSA's accepted</div>
    <div class="therapist">
      <div class="therapist-name">Dina Halpern OTR/L</div>
      <div class="therapist-phone">(718) 555-0142</div>
    </div>
  </section>
</main>
</body>
</html>
```